Email Template Design for Volmera Industrial Automation

We are looking for a skilled designer to create an engaging and visually appealing email template for Volmera Industrial Automation. The email template should be compatible with all major email clients to ensure consistent rendering across various platforms. An example email has been attached for reference, but we're open to creative interpretations that align with the brand's identity.

Deliverables:

HTML/CSS Email Template: A fully functional email template compatible with major email clients, tested for responsiveness and rendering consistency.
Images/Graphics: Any images or graphics used in the template design should be provided separately in a suitable format.

Evaluation Criteria:

Creativity and Design Aesthetics
Compatibility and Responsiveness
Alignment with Brand Identity
Clarity of Information Hierarchy
User Experience and Visual Appeal

We look forward to receiving your innovative design ideas that effectively engage and resonate with engineers in the industrial automation sector. Your contribution will play a crucial role in enhancing our email marketing efforts and promoting Volmera Industrial Automation's offerings.

Target Market(s)

Engineers in the field of industrial automation are the primary audience for this email campaign. The design should resonate with professionals who are seeking innovative solutions and products in the industrial automation sector.

Industry/Entity Type

Industrial automation

Coding

Coded - Design and coding required

Font styles to use
Sans Serif

Requirements
Must have
• 1. HTML and CSS Compatibility: The email template should be built using HTML and CSS to ensure proper rendering in different email clients. 2. Responsive Design: The template should adapt to different screen sizes, including desktop and mobile devices, to provide an optimal viewing experience. 3. Brand Consistency: The design should align with Volmera Industrial Automation's brand colors, typography, and overall visual identity. 4. Clear Call-to-Action: Include a prominent and compelling call-to-action (CTA) that drives recipients to take the desired action, such as visiting the website or exploring the featured products.
Nice to have
• - Visual Elements: Incorporate relevant images or graphics that complement the content and resonate with the industrial automation industry. - Minimalist Approach: A clean and modern design that highlights key information without overwhelming the recipient. - Dynamic Content Sections: Consider a layout that allows for customizable content sections to accommodate different campaign messages. - Brand Elements: Experiment with the integration of Volmera Industrial Automation's logo or other brand-specific elements.
Should not have
• Avoid using text as images, as this can hinder accessibility and readability. The text should be selectable and searchable within the email.

```html
<!DOCTYPE html>
<html lang="en">
<head>
<meta charset="utf-8">
<title>Volmera Industrial Automation – Newsletter</title>
<link rel="stylesheet" href="https://fonts.googleapis.com/css2?family=Rubik:wght@400;500;600&display=swap">
<style>
  :root {
    --page: #ffffff;
    --header-bg: #141d27;
    --body-bg: #17212b;
    --card-top: #141d26;
    --card-bottom: #0d141b;
    --media-bg: #1b2631;
    --heading: #8f99ac;
    --text: #a4acba;
    --muted: #8c95a6;
    --button-bg: #111920;
    --button-border: #2a3541;
    --footer-button: #10161d;
    --rule: #2c3742;
  }
  * { box-sizing: border-box; margin: 0; padding: 0; }
  html, body {
    width: 1200px; height: 3295px; overflow: hidden;
    background: var(--page);
    font-family: "Rubik", sans-serif;
  }
  .email { width: 1200px; height: 2331px; background: var(--body-bg); }

  .email-header {
    height: 92px; background: var(--header-bg);
    display: flex; align-items: center; justify-content: space-between;
    padding: 0 74px;
  }
  .brand-name { font-size: 31px; font-weight: 600; color: var(--heading); letter-spacing: 0.5px; }
  .lang-switch { display: flex; align-items: center; gap: 7px; color: var(--text); font-size: 18px; font-weight: 500; margin-right: -12px; }

  .hero-visual {
    height: 258px;
    background:
      radial-gradient(ellipse 260px 160px at 46% 55%, rgba(214,140,80,.55), transparent 70%),
      radial-gradient(ellipse 220px 120px at 62% 30%, rgba(60,110,170,.6), transparent 70%),
      linear-gradient(90deg, #2a3542 0%, #3b4553 35%, #2b3d5a 60%, #17243a 85%, #0d1626 100%);
  }

  .intro { text-align: center; padding-top: 90px; }
  .intro-title, .section-title {
    font-size: 31px; line-height: 41px; font-weight: 600; color: var(--heading);
    text-transform: uppercase;
  }
  .intro-text {
    width: 910px; margin: 24px auto 0;
    font-size: 15.5px; line-height: 26px; color: var(--text);
  }
  .btn {
    display: inline-flex; align-items: center; justify-content: center; gap: 8px;
    background: var(--button-bg); border: 1px solid var(--button-border); border-radius: 3px;
    color: var(--text); font-size: 11.5px; letter-spacing: .4px; text-transform: uppercase;
  }
  .btn-website { width: 162px; height: 39px; margin-top: 25px; }

  .products { text-align: center; padding-top: 117px; }
  .section-subtitle { margin-top: 7px; font-size: 12px; line-height: 16px; color: var(--text); }
  .product-grid {
    width: 1030px; margin: 58px auto 0;
    display: grid; grid-template-columns: repeat(3, 330px); gap: 23px 20px;
  }
  .product-card {
    height: 525px; padding: 10px; border-radius: 4px;
    background: linear-gradient(180deg, var(--card-top), var(--card-bottom));
    box-shadow: 0 0 6px rgba(0,0,0,.5), inset 0 0 0 1px #1f2a35;
  }
  .product-media {
    height: 269px; border-radius: 8px;
    box-shadow: 0 0 8px rgba(0,0,0,.35);
  }
  .media-a { background: radial-gradient(circle at 50% 50%, #4a525c 0%, #2a333d 35%, var(--media-bg) 65%); }
  .media-b { background: radial-gradient(circle at 50% 48%, #3c4148 0%, #262d35 40%, var(--media-bg) 68%); }
  .media-c { background: radial-gradient(circle at 52% 48%, #3e434b 0%, #2a3039 38%, var(--media-bg) 66%); }
  .media-d { background: radial-gradient(circle at 50% 50%, #2f5c9c 0%, #244066 35%, var(--media-bg) 66%); }
  .media-e { background: radial-gradient(circle at 50% 50%, #b5a27c 0%, #6a6352 38%, var(--media-bg) 68%); }
  .media-f { background: radial-gradient(circle at 50% 50%, #3a3f46 0%, #282e36 40%, var(--media-bg) 68%); }
  .product-name { margin-top: 26px; font-size: 19px; line-height: 24px; font-weight: 500; color: var(--heading); }
  .product-text { margin: 25px auto 0; width: 290px; font-size: 12px; line-height: 17.5px; color: var(--text); }
  .btn-details { width: 129px; height: 34px; margin-top: 26px; font-size: 10.5px; border-color: #1d2731; background: #16202a; }

  .email-footer { width: 1000px; margin: 151px auto 0; border-top: 1px solid var(--rule); }
  .footer-bar { display: flex; justify-content: space-between; align-items: center; margin-top: 18px; height: 39px; }
  .footer-links { display: flex; gap: 32px; }
  .footer-links a { color: var(--muted); font-size: 12.5px; text-decoration: underline; letter-spacing: .3px; }
  .footer-actions { display: flex; gap: 4px; }
  .footer-actions a {
    display: flex; align-items: center; height: 39px; padding: 0 16px;
    background: var(--footer-button); color: var(--text); border-radius: 3px;
    font-size: 12px; letter-spacing: .5px; text-decoration: none; text-transform: uppercase;
  }
  .footer-notes { text-align: center; margin-top: 28px; font-size: 12.5px; line-height: 26px; color: var(--text); }
</style>
</head>
<body>
<div class="email">
  <header class="email-header">
    <div class="brand-name">Volmera</div>
    <div class="lang-switch">
      <svg width="24" height="24" viewBox="0 0 24 24" fill="none" stroke="#a4acba" stroke-width="1.3">
        <circle cx="12" cy="12" r="10"/>
        <ellipse cx="12" cy="12" rx="4.5" ry="10"/>
        <line x1="2" y1="12" x2="22" y2="12"/>
        <path d="M4 6.5h16M4 17.5h16"/>
      </svg>
      <span>En</span>
      <svg width="8" height="5" viewBox="0 0 8 5"><path d="M0 0h8L4 5z" fill="#a4acba"/></svg>
    </div>
  </header>

  <div class="hero-visual" role="img" aria-label="Engineer holding a tablet beside an industrial robot arm with sparks"></div>

  <section class="intro">
    <h1 class="intro-title">Your partner for industrial networks<br>and smart control</h1>
    <p class="intro-text">Brand names alone do not impress us at all. When we select our products, the one and only thing that matters is their performance – and this is always measured against the demands and the expectations of our customers. There are many ways to arrive at the goal. We always look for the one that is the most effective and the most cost-efficient for our customers. Volmera GmbH applies a certified quality management system according to DIN EN ISO 9001:2015.</p>
    <a class="btn btn-website">Visit our website
      <svg width="18" height="8" viewBox="0 0 18 8" fill="none" stroke="#a4acba" stroke-width="1.2"><path d="M0 4h16M13 1l3 3-3 3"/></svg>
    </a>
  </section>

  <section class="products">
    <h2 class="section-title">Enim consectetur cursus</h2>
    <p class="section-subtitle">Lorem ipsum dolor sit amet consectetur.</p>
    <div class="product-grid">
      <article class="product-card">
        <div class="product-media media-a" role="img" aria-label="Transformer with red and white leads"></div>
        <h3 class="product-name">RS233 zu RS344</h3>
        <p class="product-text">Lorem ipsum dolor sit amet consectetur. Enim consectetur cursus semper volutpat dictum ut. Tempus tellus justo sed amet adipiscing auctor. Elit dolor porttitor ante dictum ac augue gravida senectus.</p>
        <a class="btn btn-details">Get details <svg width="16" height="8" viewBox="0 0 18 8" fill="none" stroke="#a4acba" stroke-width="1.2"><path d="M0 4h16M13 1l3 3-3 3"/></svg></a>
      </article>
      <article class="product-card">
        <div class="product-media media-b" role="img" aria-label="Coiled black network cable"></div>
        <h3 class="product-name">RS233 zu RS344</h3>
        <p class="product-text">Lorem ipsum dolor sit amet consectetur. Enim consectetur cursus semper volutpat dictum ut. Tempus tellus justo sed amet adipiscing auctor. Elit dolor porttitor ante dictum ac augue gravida senectus.</p>
        <a class="btn btn-details">Get details <svg width="16" height="8" viewBox="0 0 18 8" fill="none" stroke="#a4acba" stroke-width="1.2"><path d="M0 4h16M13 1l3 3-3 3"/></svg></a>
      </article>
      <article class="product-card">
        <div class="product-media media-c" role="img" aria-label="Power transformer with coloured wires"></div>
        <h3 class="product-name">RS233 zu RS344</h3>
        <p class="product-text">Lorem ipsum dolor sit amet consectetur. Enim consectetur cursus semper volutpat dictum ut. Tempus tellus justo sed amet adipiscing auctor. Elit dolor porttitor ante dictum ac augue gravida senectus.</p>
        <a class="btn btn-details">Get details <svg width="16" height="8" viewBox="0 0 18 8" fill="none" stroke="#a4acba" stroke-width="1.2"><path d="M0 4h16M13 1l3 3-3 3"/></svg></a>
      </article>
      <article class="product-card">
        <div class="product-media media-d" role="img" aria-label="Set of blue terminal block modules"></div>
        <h3 class="product-name">RS233 zu RS344</h3>
        <p class="product-text">Lorem ipsum dolor sit amet consectetur. Enim consectetur cursus semper volutpat dictum ut. Tempus tellus justo sed amet adipiscing auctor. Elit dolor porttitor ante dictum ac augue gravida senectus.</p>
        <a class="btn btn-details">Get details <svg width="16" height="8" viewBox="0 0 18 8" fill="none" stroke="#a4acba" stroke-width="1.2"><path d="M0 4h16M13 1l3 3-3 3"/></svg></a>
      </article>
      <article class="product-card">
        <div class="product-media media-e" role="img" aria-label="Printed circuit board with microcontroller"></div>
        <h3 class="product-name">RS233 zu RS344</h3>
        <p class="product-text">Lorem ipsum dolor sit amet consectetur. Enim consectetur cursus semper volutpat dictum ut. Tempus tellus justo sed amet adipiscing auctor. Elit dolor porttitor ante dictum ac augue gravida senectus.</p>
        <a class="btn btn-details">Get details <svg width="16" height="8" viewBox="0 0 18 8" fill="none" stroke="#a4acba" stroke-width="1.2"><path d="M0 4h16M13 1l3 3-3 3"/></svg></a>
      </article>
      <article class="product-card">
        <div class="product-media media-f" role="img" aria-label="Group of black rocker switches"></div>
        <h3 class="product-name">RS233 zu RS344</h3>
        <p class="product-text">Lorem ipsum dolor sit amet consectetur. Enim consectetur cursus semper volutpat dictum ut. Tempus tellus justo sed amet adipiscing auctor. Elit dolor porttitor ante dictum ac augue gravida senectus.</p>
        <a class="btn btn-details">Get details <svg width="16" height="8" viewBox="0 0 18 8" fill="none" stroke="#a4acba" stroke-width="1.2"><path d="M0 4h16M13 1l3 3-3 3"/></svg></a>
      </article>
    </div>
  </section>

  <footer class="email-footer">
    <div class="footer-bar">
      <nav class="footer-links">
        <a>LINK NAME 1</a><a>LINK NAME 2</a><a>LINK NAME 3</a><a>LINK NAME 4</a><a>LINK NAME 5</a>
      </nav>
      <div class="footer-actions">
        <a>Products</a>
        <a>Unsubscribe newsletter</a>
      </div>
    </div>
    <div class="footer-notes">
      <p>Images and text used will be changed accordingly.</p>
      <p>© 2024 Volmera Industrial Automation. All rights reserved.</p>
    </div>
  </footer>
</div>
</body>
</html>
```